Vantor Salvage looking for leading edge design not typical for our industry

We need to incorporate our new company tag line "relationships, results, reputation" into our cards. Im open to any type of design for this and colour treatment. In fact the whole card needs a new lay out including the back. "Sustainable Deconstruction" needs to be removed from the back and the new tagline used. Would like to see different text and treatment used for "Deconstruction & Demolition".

Target Market(s)

Construction

Industry/Entity Type

Construction Company

Contact Information for Business Card

Standard business card size

Font styles to use
Sans Serif

Colors
9bcb3c
0255a3
f37122

Requirements
Should not have
• Irregular sizing.

```html
<!DOCTYPE html>
<html lang="en">
<head>
<meta charset="utf-8">
<title>Vantor Salvage – Business Cards</title>
<link href="https://fonts.googleapis.com/css2?family=Arimo:wght@400;700&family=Questrial&display=swap" rel="stylesheet">
<style>
  :root {
    --page: #eceae6;
    --teal-deep: #0c6f74;
    --teal: #178a8e;
    --teal-light: #2a9a9c;
    --teal-ink: #2f7f86;
    --lime: #9bcb3c;
    --blue: #0255a3;
    --orange: #f37122;
    --card-black: #1b1b1b;
    --white: #ffffff;
  }
  * { box-sizing: border-box; margin: 0; padding: 0; }
  html, body {
    width: 1200px; height: 892px; overflow: hidden;
    background: var(--page);
  }
  .canvas { position: relative; width: 1200px; height: 892px; }

  .card {
    position: absolute; width: 560px; height: 320px;
    border-radius: 4px; overflow: hidden;
    box-shadow: 0 6px 18px rgba(0,0,0,.18);
  }

  /* Front (brand) card */
  .card--front {
    left: 570px; top: 100px;
    background: linear-gradient(135deg, var(--teal-deep) 0%, var(--teal) 55%, var(--teal-light) 100%);
  }
  .front-brand {
    position: absolute; left: 62px; top: 80px;
    display: flex; align-items: center; gap: 26px;
  }
  .front-brand__dot {
    width: 130px; height: 130px; border-radius: 50%;
    border: 12px solid var(--white);
  }
  .front-brand__name {
    font-family: "Questrial", sans-serif;
    color: var(--white); font-size: 27px; line-height: 1.15;
    letter-spacing: .5px; text-transform: uppercase;
  }
  .tagline {
    position: absolute; left: 0; right: 0; bottom: 0; height: 46px;
    background: var(--blue);
    border-top: 4px solid var(--orange);
    display: flex; align-items: center; justify-content: center;
    font-family: "Arimo", sans-serif; font-size: 15px;
    letter-spacing: 2px; text-transform: uppercase; color: var(--white);
  }
  .tagline__sep { color: var(--orange); margin: 0 10px; }

  /* Back (contact) card */
  .card--back { left: 80px; top: 450px; background: var(--card-black); }
  .card__arcs { position: absolute; inset: 0; }
  .back-content {
    position: absolute; left: 0; right: 0; top: 26px;
    text-align: center; color: var(--white);
  }
  .back-brand__dot {
    width: 88px; height: 88px; border-radius: 50%;
    border: 9px solid var(--teal-ink); margin: 0 auto 8px;
  }
  .back-brand__name {
    font-family: "Questrial", sans-serif;
    color: var(--teal-ink); font-size: 22px; line-height: 1.1;
    text-transform: uppercase; letter-spacing: .5px;
  }
  .person {
    font-family: "Arimo", sans-serif; font-weight: 700;
    font-size: 25px; margin-top: 10px; line-height: 1;
  }
  .person-title {
    font-family: "Arimo", sans-serif; font-size: 17px; margin-top: 2px;
  }
  .contact {
    font-family: "Arimo", sans-serif; font-size: 13px; line-height: 1.3;
    margin-top: 8px;
  }
</style>
</head>
<body>
<main class="canvas">

  <section class="card card--front" aria-label="Business card front">
    <div class="front-brand">
      <div class="front-brand__dot"></div>
      <p class="front-brand__name">Vantor Salvage<br>&amp; Demolition Inc.</p>
    </div>
    <p class="tagline">Relationships<span class="tagline__sep">•</span>Results<span class="tagline__sep">•</span>Reputation</p>
  </section>

  <section class="card card--back" aria-label="Business card back">
    <svg class="card__arcs" width="560" height="320" viewBox="0 0 560 320" aria-hidden="true">
      <circle cx="280" cy="190" r="236" fill="none" stroke="var(--lime)" stroke-width="13"/>
      <circle cx="280" cy="190" r="224" fill="none" stroke="var(--teal-ink)" stroke-width="8"/>
    </svg>
    <div class="back-content">
      <div class="back-brand__dot"></div>
      <p class="back-brand__name">Vantor Salvage<br>&amp; Demolition Inc.</p>
      <p class="person">Owen Marsh</p>
      <p class="person-title">Head Estimater</p>
      <p class="contact">
        www.vantorsalvage.com<br>
        owenm@vantorsalvage.com<br>
        (555) 014 2290 | (555) 017 4415 | (555) 013 8802<br>
        #100, 4820-72 Street Halvern, AB T0X 1K4
      </p>
    </div>
  </section>

</main>
</body>
</html>
```